I-71 Website for Washington D.C Cannabis Business

We need a website with a 21+ age (yes/no/captcha) verification
5 Pages listed on a top banner
Home/Splash Page-Should send back to splash & ask for 21+ veri
Shop-
about Us
Blog
Contact us:

Content for pages:
Splash Page - Contains How it works with 1-6 steps
1. Register for Rewards Or Head to {Link} for more anonymous Use
2. Choose Cookies & Free Gifts
3. Submit Address & Order
4.Recieve Confirmation Text
5.Send Separate Selfie and Clear Drivers License Picture
6.Enjoy Your Cookies and Free Gifts

Shop/Menu Page - Empty with top banner (will fill in this section)

Home- Should link back to Splash page
About Us-
"Welcome to Maple Parcel, where everyday is a maple day! We believe that everyone who chooses to enjoy the medicinal and relaxing benefits cannabis, should have safe and reliable access. And no matter your lifestyle or level of wellness, you deserve access to friendly customer service and professional courtesy. At Maple Parcel we provide Artisan Cookies that come with I-71 Gifted premium exotic cannabis + edibles & accessories. We provide an excellent variety of cookies and gifts, and all purchases improve your community!

For every 5 Cookies you purchase we donate 50 Sandwiches to Local DC Organizations that help our community members in need. In this way, you’ll be supporting the local DC community by purchasing from Maple Parcel (We also have Sandwich Rewards!!)

Maple Parcel is and always will be committed to providing DC The Best Service, Gifts & Experience. Always. We are committed to setting a standard for the gifting business in DC.

We appreciate you taking the time to check us out! We are here for all of your I-71 compliant needs.

Need to reach us? Please send all business related inquiries/compliments/complaints to Mapleparceldc@velnormail.com and we will reach out ASAP. We look forward to hearing from you!

-MP

Blog- This should be Fillable
Contact US: Should be fillable with text or graphic

Similar Websites to check out: https://www.dcqenlowfarm.com/
https://www.amberloftvista.com/

Target Market(s)

DC/Cannabis market

Coding

Coded - Design and coding required

Number of Pages Required

5+ page

Font styles to use
Other font styles liked:
• Sans Serif

Colors
0455a3
33b8a4
ffffff

Requirements
Must have
• 21+ age (yes/no/captcha) verification
I-71 Compliant
Color match the green to the logo
Nice to have
• I would like the website to have a fresh and fun look....without being corny
Cookie buttons (menu etc that look like a cookie)
Should not have
• No pictures of Marihuana

```html
<!DOCTYPE html>
<html lang="en">
<head>
<meta charset="utf-8">
<title>Maple Parcel – Home</title>
<link href="https://fonts.googleapis.com/css2?family=Montserrat:wght@400;500;600;700;800&family=Roboto:wght@400;500&family=Yellowtail&display=swap" rel="stylesheet">
<style>
  :root{
    --blue:#0455a3;
    --teal:#33b8a4;
    --white:#ffffff;
    --green:#1fd81a;
    --ink:#3a3a3a;
    --backdrop:#ebebeb;
    --grey-btn:#c4c4c4;
    --footer:#0659a8;
  }
  *{box-sizing:border-box;margin:0;padding:0}
  html,body{width:1200px;height:938px;overflow:hidden;background:var(--backdrop)}
  body{position:relative;font-family:'Roboto',sans-serif;color:var(--ink)}

  .page{position:absolute;top:59px;width:560px;height:794px;background:var(--white);overflow:hidden}
  .page--gated{left:30px}
  .page--open{left:609px}
  .page--gated::after{content:"";position:absolute;inset:0;background:rgba(0,0,0,.62);z-index:5}

  .site-header{position:absolute;left:0;top:0;width:560px;height:59px;background:var(--white);z-index:3}
  .brand-tab{position:absolute;left:42px;top:0;width:127px;height:72px;background:var(--white);
    clip-path:polygon(0 0,100% 0,100% 82%,92% 100%,8% 100%,0 82%);z-index:3;
    display:flex;flex-direction:column;align-items:center;justify-content:center;gap:5px;padding-top:6px}
  .brand-mark{width:22px;height:22px;border-radius:50%;background:var(--green)}
  .brand-name{font-family:'Montserrat',sans-serif;font-weight:700;font-size:8.5px;color:var(--blue);letter-spacing:.3px}

  .main-nav{position:absolute;top:0;left:0;height:59px;width:560px;font-family:'Montserrat',sans-serif;font-size:6.6px;font-weight:500;color:#333}
  .main-nav a{position:absolute;top:26px;color:inherit;text-decoration:none;transform:translateX(-50%);white-space:nowrap}
  .main-nav a.is-active{color:var(--blue)}
  .cart{position:absolute;left:482px;top:16px;width:27px;height:27px;border-radius:50%;background:var(--blue)}
  .cart span{position:absolute;left:0;right:0;top:4px;text-align:center;color:var(--white);font-size:6px}
  .cart svg{position:absolute;left:9px;top:12px}

  .hero{position:absolute;left:0;top:59px;width:560px;height:331px;
    background:radial-gradient(ellipse at 62% 45%,#8a6240 0%,#5a3e28 40%,#2f2118 80%,#231913 100%)}
  .hero__title{position:absolute;left:0;right:0;top:104px;text-align:center;font-family:'Montserrat',sans-serif;font-weight:800;font-size:31px;color:var(--white);letter-spacing:.5px}
  .hero__tagline{position:absolute;left:0;right:0;top:139px;text-align:center;font-family:'Yellowtail',cursive;font-size:27px;color:var(--green)}
  .hero__cta{position:absolute;left:237px;top:248px;width:87px;height:28px;border:2px solid var(--green);border-radius:16px;background:var(--white);
    font-family:'Montserrat',sans-serif;font-weight:700;font-size:8.5px;color:#222;display:flex;align-items:center;justify-content:center}

  .how{position:absolute;left:0;top:390px;width:560px;height:362px}
  .how__title{position:absolute;left:0;right:0;top:28px;text-align:center;font-family:'Montserrat',sans-serif;font-weight:700;font-size:15.5px;color:var(--blue)}
  .how__lede{position:absolute;left:0;right:0;top:50px;text-align:center;font-family:'Yellowtail',cursive;font-size:12px;color:var(--teal)}
  .step-label{position:absolute;font-family:'Montserrat',sans-serif;font-size:7.2px;line-height:11.5px;text-align:center;color:#333;transform:translateX(-50%);white-space:nowrap}
  .steps{position:absolute;left:0;top:135px}
  .how__cta{position:absolute;left:227px;top:298px;width:106px;height:31px;border-radius:16px;
    background:linear-gradient(90deg,var(--blue),var(--teal));color:var(--white);
    font-family:'Montserrat',sans-serif;font-weight:500;font-size:7px;display:flex;align-items:center;justify-content:center}

  .site-footer{position:absolute;left:0;top:752px;width:560px;height:42px;background:var(--footer);color:var(--white);
    font-size:7.3px;display:flex;align-items:center;justify-content:center}

  .age-gate{position:absolute;left:122px;top:152px;width:316px;height:194px;background:var(--white);z-index:6;text-align:center}
  .age-gate .brand-mark{position:absolute;left:146px;top:14px;width:26px;height:26px}
  .age-gate__name{position:absolute;left:0;right:0;top:47px;font-family:'Montserrat',sans-serif;font-weight:700;font-size:9px;color:var(--blue)}
  .age-gate__text{position:absolute;left:30px;right:30px;top:85px;font-size:7.8px;line-height:14px;color:#333}
  .age-gate__question{position:absolute;left:0;right:0;top:122px;font-family:'Montserrat',sans-serif;font-weight:600;font-size:12.3px;color:#333}
  .age-gate__btn{position:absolute;top:150px;width:85px;height:24px;border:0;color:var(--white);
    font-family:'Montserrat',sans-serif;font-weight:600;font-size:11px;display:flex;align-items:center;justify-content:center}
  .age-gate__btn--no{left:70px;background:var(--grey-btn)}
  .age-gate__btn--yes{left:161px;background:var(--blue)}
</style>
</head>
<body>

<!-- Age gate state -->
<section class="page page--gated">
  <header class="site-header">
    <nav class="main-nav">
      <a class="is-active" style="left:262px">HOME</a>
      <a style="left:304px">SHOP</a>
      <a style="left:353px">ABOUT US</a>
      <a style="left:402px">BLOG</a>
      <a style="left:454px">CONTACT US</a>
    </nav>
    <div class="cart"><span>0</span>
      <svg width="9" height="8" viewBox="0 0 9 8"><path d="M0 1h2l1 4h5l1-3H2.5" fill="none" stroke="#fff" stroke-width="1"/><circle cx="3.5" cy="7" r=".8" fill="#fff"/><circle cx="7" cy="7" r=".8" fill="#fff"/></svg>
    </div>
  </header>
  <div class="brand-tab"><span class="brand-mark"></span><span class="brand-name">MAPLE PARCEL</span></div>
  <div class="hero" role="img" aria-label="Photo of wrapped gift boxes, gingerbread cookies and a mug of hot cocoa with marshmallows"></div>

  <section class="how">
    <h2 class="how__title">HOW IT WORKS</h2>
    <p class="how__lede">Sed ut perspiciatis unde omnis iste natus error sit</p>
    <p class="step-label" style="left:168px;top:102px">CHOOSE COOKIES<br>&amp; FREE GIFTS</p>
    <p class="step-label" style="left:313px;top:102px">RECIEVE<br>CONFIRMATION TEXT</p>
    <p class="step-label" style="left:469px;top:102px">ENJOY YOUR COOKIES<br>&amp; FREE GIFTS</p>
    <svg class="steps" width="560" height="100" viewBox="0 0 560 100">
      <g fill="none" stroke="#222" stroke-width="1">
        <path d="M60 45A37 37 0 0 0 134 45"/><path d="M60 45A37 37 0 0 1 134 45" stroke-dasharray="1 3"/>
        <path d="M135 45A37 37 0 0 1 209 45"/><path d="M135 45A37 37 0 0 0 209 45" stroke-dasharray="1 3"/>
        <path d="M210 45A37 37 0 0 0 284 45"/><path d="M210 45A37 37 0 0 1 284 45" stroke-dasharray="1 3"/>
        <path d="M286 45A37 37 0 0 1 360 45"/><path d="M286 45A37 37 0 0 0 360 45" stroke-dasharray="1 3"/>
        <path d="M361 45A37 37 0 0 0 435 45"/><path d="M361 45A37 37 0 0 1 435 45" stroke-dasharray="1 3"/>
        <path d="M437 45A37 37 0 0 1 511 45"/><path d="M437 45A37 37 0 0 0 511 45" stroke-dasharray="1 3"/>
        <rect x="83" y="44" width="28" height="10"/><rect x="88" y="32" width="16" height="12"/><path d="M91 36h10M91 40h10M86 57h24"/>
        <circle cx="172" cy="45" r="14"/><circle cx="167" cy="41" r="1.5"/><circle cx="176" cy="44" r="1.5"/><circle cx="170" cy="51" r="1.5"/>
        <rect x="236" y="32" width="18" height="24"/><path d="M240 40h10M240 45h10M240 50h8"/><circle cx="256" cy="34" r="6"/><path d="M256 31v3h2"/>
        <rect x="309" y="36" width="28" height="20"/><path d="M309 36l14 10 14-10M309 56l10-9M337 56l-10-9"/>
        <rect x="382" y="34" width="32" height="22" rx="2"/><circle cx="392" cy="42" r="3"/><path d="M386 52c1-4 11-4 12 0M401 40h9M401 45h9M401 50h7"/>
        <rect x="461" y="40" width="26" height="18"/><rect x="459" y="35" width="30" height="5"/><path d="M474 35v23M474 35c-4-6-10-4-6 0M474 35c4-6 10-4 6 0"/>
      </g>
      <defs><linearGradient id="badge-a" x1="0" y1="0" x2="0" y2="1"><stop offset="0" stop-color="#33b8a4"/><stop offset="1" stop-color="#0455a3"/></linearGradient></defs>
      <g font-family="Montserrat,sans-serif" font-size="8.5" font-weight="600" fill="#fff" text-anchor="middle">
        <circle cx="63" cy="36" r="14" fill="url(#badge-a)"/><text x="63" y="39">01</text>
        <circle cx="157" cy="10" r="14" fill="url(#badge-a)"/><text x="157" y="13">02</text>
        <circle cx="231" cy="77" r="14" fill="url(#badge-a)"/><text x="231" y="80">03</text>
        <circle cx="307" cy="10" r="14" fill="url(#badge-a)"/><text x="307" y="13">04</text>
        <circle cx="382" cy="77" r="14" fill="url(#badge-a)"/><text x="382" y="80">05</text>
        <circle cx="457" cy="10" r="14" fill="url(#badge-a)"/><text x="457" y="13">06</text>
      </g>
    </svg>
    <p class="step-label" style="left:91px;top:242px">REGISTER FOR<br>REWARDS</p>
    <p class="step-label" style="left:247px;top:244px">SUBMIT ADDRESS<br>&amp; ORDER</p>
    <p class="step-label" style="left:399px;top:244px">SEND SEPARATE<br>SELFIE AND&amp; CLEAR DRIVERS<br>LICENSE PICTURE</p>
    <div class="how__cta">CONTINUE TO SHOP</div>
  </section>
  <footer class="site-footer">© Copyrights 2021 Maple Parcel.All Rights Reserved.</footer>

  <div class="age-gate" role="dialog" aria-label="Age verification">
    <span class="brand-mark"></span>
    <p class="age-gate__name">MAPLE PARCEL</p>
    <p class="age-gate__text">But I must explain to you how all this mistaken idea of denouncing pain was born and I will give you a complete account</p>
    <p class="age-gate__question">YOU MUST BE 18 OLD TO ENTER</p>
    <div class="age-gate__btn age-gate__btn--no">NO</div>
    <div class="age-gate__btn age-gate__btn--yes">YES</div>
  </div>
</section>

<!-- Open state -->
<section class="page page--open">
  <header class="site-header">
    <nav class="main-nav">
      <a class="is-active" style="left:262px">HOME</a>
      <a style="left:304px">SHOP</a>
      <a style="left:353px">ABOUT US</a>
      <a style="left:402px">BLOG</a>
      <a style="left:454px">CONTACT US</a>
    </nav>
    <div class="cart"><span>0</span>
      <svg width="9" height="8" viewBox="0 0 9 8"><path d="M0 1h2l1 4h5l1-3H2.5" fill="none" stroke="#fff" stroke-width="1"/><circle cx="3.5" cy="7" r=".8" fill="#fff"/><circle cx="7" cy="7" r=".8" fill="#fff"/></svg>
    </div>
  </header>
  <div class="brand-tab"><span class="brand-mark"></span><span class="brand-name">MAPLE PARCEL</span></div>
  <div class="hero" role="img" aria-label="Photo of wrapped gift boxes, gingerbread cookies and a mug of hot cocoa with marshmallows">
    <h1 class="hero__title">MAPLE PARCEL</h1>
    <p class="hero__tagline">Where everyday is a maple day</p>
    <div class="hero__cta">SHOP NOW</div>
  </div>

  <section class="how">
    <h2 class="how__title">HOW IT WORKS</h2>
    <p class="how__lede">Sed ut perspiciatis unde omnis iste natus error sit</p>
    <p class="step-label" style="left:168px;top:102px">CHOOSE COOKIES<br>&amp; FREE GIFTS</p>
    <p class="step-label" style="left:313px;top:102px">RECIEVE<br>CONFIRMATION TEXT</p>
    <p class="step-label" style="left:469px;top:102px">ENJOY YOUR COOKIES<br>&amp; FREE GIFTS</p>
    <svg class="steps" width="560" height="100" viewBox="0 0 560 100">
      <g fill="none" stroke="#222" stroke-width="1">
        <path d="M60 45A37 37 0 0 0 134 45"/><path d="M60 45A37 37 0 0 1 134 45" stroke-dasharray="1 3"/>
        <path d="M135 45A37 37 0 0 1 209 45"/><path d="M135 45A37 37 0 0 0 209 45" stroke-dasharray="1 3"/>
        <path d="M210 45A37 37 0 0 0 284 45"/><path d="M210 45A37 37 0 0 1 284 45" stroke-dasharray="1 3"/>
        <path d="M286 45A37 37 0 0 1 360 45"/><path d="M286 45A37 37 0 0 0 360 45" stroke-dasharray="1 3"/>
        <path d="M361 45A37 37 0 0 0 435 45"/><path d="M361 45A37 37 0 0 1 435 45" stroke-dasharray="1 3"/>
        <path d="M437 45A37 37 0 0 1 511 45"/><path d="M437 45A37 37 0 0 0 511 45" stroke-dasharray="1 3"/>
        <rect x="83" y="44" width="28" height="10"/><rect x="88" y="32" width="16" height="12"/><path d="M91 36h10M91 40h10M86 57h24"/>
        <circle cx="172" cy="45" r="14"/><circle cx="167" cy="41" r="1.5"/><circle cx="176" cy="44" r="1.5"/><circle cx="170" cy="51" r="1.5"/>
        <rect x="236" y="32" width="18" height="24"/><path d="M240 40h10M240 45h10M240 50h8"/><circle cx="256" cy="34" r="6"/><path d="M256 31v3h2"/>
        <rect x="309" y="36" width="28" height="20"/><path d="M309 36l14 10 14-10M309 56l10-9M337 56l-10-9"/>
        <rect x="382" y="34" width="32" height="22" rx="2"/><circle cx="392" cy="42" r="3"/><path d="M386 52c1-4 11-4 12 0M401 40h9M401 45h9M401 50h7"/>
        <rect x="461" y="40" width="26" height="18"/><rect x="459" y="35" width="30" height="5"/><path d="M474 35v23M474 35c-4-6-10-4-6 0M474 35c4-6 10-4 6 0"/>
      </g>
      <defs><linearGradient id="badge-b" x1="0" y1="0" x2="0" y2="1"><stop offset="0" stop-color="#33b8a4"/><stop offset="1" stop-color="#0455a3"/></linearGradient></defs>
      <g font-family="Montserrat,sans-serif" font-size="8.5" font-weight="600" fill="#fff" text-anchor="middle">
        <circle cx="63" cy="36" r="14" fill="url(#badge-b)"/><text x="63" y="39">01</text>
        <circle cx="157" cy="10" r="14" fill="url(#badge-b)"/><text x="157" y="13">02</text>
        <circle cx="231" cy="77" r="14" fill="url(#badge-b)"/><text x="231" y="80">03</text>
        <circle cx="307" cy="10" r="14" fill="url(#badge-b)"/><text x="307" y="13">04</text>
        <circle cx="382" cy="77" r="14" fill="url(#badge-b)"/><text x="382" y="80">05</text>
        <circle cx="457" cy="10" r="14" fill="url(#badge-b)"/><text x="457" y="13">06</text>
      </g>
    </svg>
    <p class="step-label" style="left:91px;top:242px">REGISTER FOR<br>REWARDS</p>
    <p class="step-label" style="left:247px;top:244px">SUBMIT ADDRESS<br>&amp; ORDER</p>
    <p class="step-label" style="left:399px;top:244px">SEND SEPARATE<br>SELFIE AND&amp; CLEAR DRIVERS<br>LICENSE PICTURE</p>
    <div class="how__cta">CONTINUE TO SHOP</div>
  </section>
  <footer class="site-footer">© Copyrights 2021 Maple Parcel.All Rights Reserved.</footer>
</section>

</body>
</html>
```